Business card, letterhead, envelope design, email footer for non-profit private equity association
Riviera Growth Capital and Seed Funding Society
Business card, letterhead, envelope design, email footer for non-profit private equity association - Financial Services
Creative Brief
Simple
Tobias Hernquist
Head of Operations
17, Rue des Orangers 98000 Monaco
thernquist@rgsf-example.org
www.rgsf-example.org
Stationery will be prepared for all 7-8 Board Members of our non-profit association. The stationery design is a subsequent process of the new logo design, which has just been created. The Riviera Growth Capital & Seed Funding Society (RGSF) stands for: seriousness and professionalism. Our official website is http://www.rgsf-example.org Please note that this website still includes the OLD logo and layout (to be changed shortly, so please do not let that influence you. This is more to show you the content rather than the design.

```html
<!DOCTYPE html>
<html lang="en">
<head>
<meta charset="utf-8">
<title>RGSF Business Card</title>
<link href="https://fonts.googleapis.com/css2?family=Montserrat:wght@800&family=Open+Sans:wght@400;600&display=swap" rel="stylesheet">
<style>
  :root {
    --backdrop: #3b3b3d;
    --card-white: #ffffff;
    --band-dark: #2e2e30;
    --accent-red: #d7262e;
    --ink: #2b2b2d;
    --ink-soft: #4a4a4c;
  }
  * { margin: 0; padding: 0; box-sizing: border-box; }
  html, body { width: 1200px; height: 782px; overflow: hidden; }
  body { background: var(--backdrop); position: relative; font-family: "Open Sans", sans-serif; }

  .card {
    position: absolute;
    width: 540px;
    height: 310px;
    background: var(--card-white);
    border-radius: 24px;
    overflow: hidden;
  }
  .card--back { left: 40px; top: 70px; }
  .card--front { left: 620px; top: 400px; }
  .card-shape { position: absolute; inset: 0; width: 100%; height: 100%; }

  .brand { position: absolute; color: var(--ink); font-family: "Montserrat", sans-serif; font-weight: 800; }
  .brand-mark { display: block; font-size: 58px; line-height: 1; letter-spacing: 1px; }
  .brand-name { display: block; font-size: 11.5px; line-height: 1.3; text-transform: uppercase; margin-top: 6px; width: 270px; }
  .card--back .brand { left: 58px; top: 142px; }
  .card--front .brand { left: 36px; top: 138px; }
  .card--front .brand-mark { font-size: 52px; }
  .card--front .brand-name { width: 230px; font-size: 10.5px; }

  .holder { position: absolute; right: 30px; top: 22px; text-align: right; color: var(--card-white); }
  .holder-name { font-size: 15px; font-weight: 600; }
  .holder-role { font-size: 12px; margin-top: 2px; }

  .divider { position: absolute; left: 300px; top: 138px; width: 1px; height: 140px; background: var(--accent-red); }

  .contact { position: absolute; left: 314px; top: 136px; list-style: none; color: var(--ink-soft); font-size: 12.5px; line-height: 1.35; }
  .contact li { display: flex; align-items: flex-start; gap: 6px; margin-bottom: 3px; }
  .contact svg { width: 11px; height: 11px; flex: none; margin-top: 3px; fill: var(--accent-red); }
  .contact .no-icon { padding-left: 0; }
</style>
</head>
<body>

  <section class="card card--back" aria-label="Business card back">
    <svg class="card-shape" viewBox="0 0 540 310" preserveAspectRatio="none" aria-hidden="true">
      <path d="M0 0 H540 V34 C380 36 200 58 0 112 Z" fill="var(--band-dark)"/>
      <path d="M0 120 C200 68 380 46 540 44 V52 C380 56 200 80 0 130 Z" fill="var(--accent-red)"/>
    </svg>
    <div class="brand">
      <span class="brand-mark">RGSF</span>
      <span class="brand-name">Riviera Growth Capital and Seed Funding Society</span>
    </div>
  </section>

  <section class="card card--front" aria-label="Business card front">
    <svg class="card-shape" viewBox="0 0 540 310" preserveAspectRatio="none" aria-hidden="true">
      <path d="M0 0 H540 V112 C380 66 200 48 0 50 Z" fill="var(--band-dark)"/>
      <path d="M0 58 C200 56 380 76 540 120 V128 C380 86 200 66 0 68 Z" fill="var(--accent-red)"/>
    </svg>
    <div class="holder">
      <p class="holder-name">Marlo Quintaine</p>
      <p class="holder-role">Consultant</p>
    </div>
    <div class="brand">
      <span class="brand-mark">RGSF</span>
      <span class="brand-name">Riviera Growth Capital and Seed Funding Society</span>
    </div>
    <span class="divider"></span>
    <ul class="contact">
      <li><span>045, 12th floor,<br>Harbour View Road</span></li>
      <li><svg viewBox="0 0 12 12"><path d="M2.5 1 L4.5 1 L5.3 3.4 L4 4.5 C4.7 6 6 7.3 7.5 8 L8.6 6.7 L11 7.5 L11 9.5 C11 10.3 10.3 11 9.5 11 C5 11 1 7 1 2.5 C1 1.7 1.7 1 2.5 1 Z"/></svg><span>010 555 0142</span></li>
      <li><svg viewBox="0 0 12 12"><path d="M1 2.5 H11 V9.5 H1 Z M1.6 3 L6 6.4 L10.4 3 V3.8 L6 7.2 L1.6 3.8 Z" fill-rule="evenodd"/></svg><span>010 555 0142</span></li>
      <li><svg viewBox="0 0 12 12"><path d="M1 2.5 H11 L6 6.5 Z M1 3.6 L6 7.6 L11 3.6 V9.5 H1 Z"/></svg><span>yourname@example.com</span></li>
      <li><span>www.example-site.com</span></li>
    </ul>
  </section>

</body>
</html>
```